New Phone Case requires logo and packaging

We need a nice and sleek logo designed along with packaging for our Premium Phone Case brand

Our Brand Name is Vaxel
Please note this has nothing to do with a Rhino so don't put a Rhino in the logo
I've also attached a file called VAXEL Logo Inspiration, which shows something along the lines of the type of text we want to use. Please note i have photoshopped that image together from another logo we had, and i liked the text, but its for you to see what direction we want to go in. Also note i have shown different variations in that image file, use your imagination with it and show us a nice and clean logo.

We would like the Brand in upper caps such as VAXEL
The brand is for Premium Phone Cases. The first thing that should come to someones mind when looking at the branding is High Quality, Premium and Modern.

The look must be high end and modern

The design must portray high quality and premium!

Also i will say "Less is More". Don't cramp many things on the packaging and logo. We just want a nice, clean cut high quality logo and packaging

I have attached images of an example packaging from a few competitors. One is a standard open from top packaging, while another is a slide out packaging. Our packaging dimensions should be the same which are Packaging dimensions
Length = 18cm
Height = 1.5cm
Depth = 9.5cm

Also note the example packaging has a transparent front section to show which case is inside, this is optional if you want to have it. If not you can cover it all up.

Font styles to use
Other font styles liked:
• Any nice font but just not the standard everyday stuff like Arial, San Serif etc as i want it to be differentiated. A Font that shows Serious Quality and one that stands out would be awesome!

Colors

Designer to choose colors to be used in the design.

Requirements
Must have
• Must be a nice and clean design
• Packaging dimensions
• Length = 18cm
• Height = 1.5cm
• Depth = 9.5cm

```html
<!DOCTYPE html>
<html lang="en">
<head>
<meta charset="utf-8">
<title>Vaxel Packaging</title>
<link href="https://fonts.googleapis.com/css2?family=Orbitron:wght@500;700;800&family=Arimo:wght@400&display=swap" rel="stylesheet">
<style>
  :root {
    --ink: #111111;
    --paper: #ffffff;
    --sleeve-top: #ffffff;
    --sleeve-bottom: #e9e9eb;
    --line: #b9b9bd;
    --grey-1: #555558;
    --grey-2: #8a8a8e;
    --grey-3: #c4c4c7;
    --case-black: #2a2a2c;
    --case-blue: #4f78df;
    --case-red: #e2685f;
    --case-white: #f7f7f7;
    --case-orange: #e2895d;
    --case-purple: #d466dc;
    --font: "Orbitron", sans-serif;
    --font-label: "Arimo", sans-serif;
  }
  * { box-sizing: border-box; margin: 0; padding: 0; }
  html, body { width: 1200px; height: 1200px; overflow: hidden; background: var(--paper); font-family: var(--font); color: var(--ink); }

  .range {
    position: absolute; left: 60px; top: 40px;
    display: grid; grid-template-columns: repeat(3, 340px); grid-template-rows: repeat(2, 330px);
    gap: 30px;
  }
  .sleeve {
    position: relative; border: 1px solid #d2d2d5;
    background: linear-gradient(160deg, var(--sleeve-top), var(--sleeve-bottom));
    overflow: hidden;
  }
  .sleeve__brand {
    position: absolute; right: 18px; top: 10px;
    font-weight: 700; font-size: 17px; letter-spacing: 1px;
  }
  .sleeve__band {
    position: absolute; left: 0; right: 0; top: 36px; height: 22px;
    background: var(--ink); color: var(--paper);
    font-size: 11px; font-weight: 700; letter-spacing: 1px;
    display: flex; align-items: center; justify-content: center;
  }
  .sleeve__layers { position: absolute; left: 30px; top: 66px; }
  .badge {
    position: absolute; left: 30px;
    border: 1px solid var(--line); border-radius: 6px;
    font-size: 9px; font-weight: 500; text-align: center; line-height: 1.25;
    color: #333; padding: 4px 8px;
  }
  .badge--layer { top: 170px; width: 104px; }
  .badge__num {
    position: absolute; left: 0; right: 0; top: -27px; text-align: center;
    font-size: 24px; font-weight: 800; color: var(--ink); line-height: 1;
  }
  .badge--scratch { top: 210px; width: 96px; }
  .badge--top {
    top: 250px; left: 56px; width: 76px; border: none;
    background: var(--ink); color: var(--paper); border-radius: 8px; padding: 4px 0;
  }
  .badge__big { display: block; font-size: 17px; font-weight: 800; line-height: 1.1; }
  .badge__small { display: block; font-size: 8px; }
  .sleeve__window {
    position: absolute; right: 40px; top: 76px; width: 120px; height: 196px;
    background: var(--ink); padding-left: 26px;
  }
  .sleeve__case {
    display: block; height: 100%;
    border-left: 3px solid #9a9a9d;
    background: var(--case);
  }
  .sleeve__claim {
    position: absolute; left: 0; right: 0; bottom: 10px; text-align: center;
    font-size: 10.5px; font-weight: 500; letter-spacing: 0.5px; color: #222;
  }
  .case-black { --case: var(--case-black); }
  .case-blue { --case: var(--case-blue); }
  .case-red { --case: var(--case-red); }
  .case-white { --case: var(--case-white); }
  .case-orange { --case: var(--case-orange); }
  .case-purple { --case: var(--case-purple); }

  .versions__title {
    position: absolute; left: 0; right: 0; top: 830px; text-align: center;
    font-family: var(--font-label); font-size: 27px; font-weight: 400; letter-spacing: 0.5px;
  }
  .versions__tile {
    position: absolute; width: 352px; height: 118px;
    display: flex; align-items: center; justify-content: center;
    font-size: 48px; letter-spacing: 2px;
  }
  .tile--a { left: 244px; top: 909px; background: var(--ink); color: var(--paper); font-weight: 500; }
  .tile--b { left: 596px; top: 909px; width: 360px; color: var(--ink); font-weight: 800; }
  .tile--c { left: 244px; top: 1027px; color: var(--ink); font-weight: 500; }
  .tile--d { left: 596px; top: 1027px; width: 360px; background: var(--ink); color: var(--paper); font-weight: 800; }
</style>
</head>
<body>
  <main class="range">
    <article class="sleeve case-black">
      <div class="sleeve__brand">VAXEL</div>
      <div class="sleeve__band">PHONE CASE PROTECTION</div>
      <svg class="sleeve__layers" width="72" height="70" viewBox="0 0 72 70" aria-hidden="true">
        <rect x="0" y="14" width="46" height="52" rx="7" fill="var(--grey-3)"/>
        <rect x="9" y="8" width="46" height="52" rx="7" fill="var(--grey-2)"/>
        <rect x="18" y="2" width="46" height="52" rx="7" fill="var(--grey-1)"/>
      </svg>
      <div class="badge badge--layer"><span class="badge__num">2</span>EXTRA LAYER<br>PROTECTION</div>
      <div class="badge badge--scratch">SCRATCH<br>RESISTANT</div>
      <div class="badge badge--top"><span class="badge__big">TOP</span><span class="badge__small">QUALITY</span></div>
      <div class="sleeve__window"><span class="sleeve__case"></span></div>
      <div class="sleeve__claim">COMPATIBLE WITH 99% PHONES</div>
    </article>
    <article class="sleeve case-blue">
      <div class="sleeve__brand">VAXEL</div>
      <div class="sleeve__band">PHONE CASE PROTECTION</div>
      <svg class="sleeve__layers" width="72" height="70" viewBox="0 0 72 70" aria-hidden="true">
        <rect x="0" y="14" width="46" height="52" rx="7" fill="var(--grey-3)"/>
        <rect x="9" y="8" width="46" height="52" rx="7" fill="var(--grey-2)"/>
        <rect x="18" y="2" width="46" height="52" rx="7" fill="var(--grey-1)"/>
      </svg>
      <div class="badge badge--layer"><span class="badge__num">2</span>EXTRA LAYER<br>PROTECTION</div>
      <div class="badge badge--scratch">SCRATCH<br>RESISTANT</div>
      <div class="badge badge--top"><span class="badge__big">TOP</span><span class="badge__small">QUALITY</span></div>
      <div class="sleeve__window"><span class="sleeve__case"></span></div>
      <div class="sleeve__claim">COMPATIBLE WITH 99% PHONES</div>
    </article>
    <article class="sleeve case-red">
      <div class="sleeve__brand">VAXEL</div>
      <div class="sleeve__band">PHONE CASE PROTECTION</div>
      <svg class="sleeve__layers" width="72" height="70" viewBox="0 0 72 70" aria-hidden="true">
        <rect x="0" y="14" width="46" height="52" rx="7" fill="var(--grey-3)"/>
        <rect x="9" y="8" width="46" height="52" rx="7" fill="var(--grey-2)"/>
        <rect x="18" y="2" width="46" height="52" rx="7" fill="var(--grey-1)"/>
      </svg>
      <div class="badge badge--layer"><span class="badge__num">2</span>EXTRA LAYER<br>PROTECTION</div>
      <div class="badge badge--scratch">SCRATCH<br>RESISTANT</div>
      <div class="badge badge--top"><span class="badge__big">TOP</span><span class="badge__small">QUALITY</span></div>
      <div class="sleeve__window"><span class="sleeve__case"></span></div>
      <div class="sleeve__claim">COMPATIBLE WITH 99% PHONES</div>
    </article>
    <article class="sleeve case-white">
      <div class="sleeve__brand">VAXEL</div>
      <div class="sleeve__band">PHONE CASE PROTECTION</div>
      <svg class="sleeve__layers" width="72" height="70" viewBox="0 0 72 70" aria-hidden="true">
        <rect x="0" y="14" width="46" height="52" rx="7" fill="var(--grey-3)"/>
        <rect x="9" y="8" width="46" height="52" rx="7" fill="var(--grey-2)"/>
        <rect x="18" y="2" width="46" height="52" rx="7" fill="var(--grey-1)"/>
      </svg>
      <div class="badge badge--layer"><span class="badge__num">2</span>EXTRA LAYER<br>PROTECTION</div>
      <div class="badge badge--scratch">SCRATCH<br>RESISTANT</div>
      <div class="badge badge--top"><span class="badge__big">TOP</span><span class="badge__small">QUALITY</span></div>
      <div class="sleeve__window"><span class="sleeve__case"></span></div>
      <div class="sleeve__claim">COMPATIBLE WITH 99% PHONES</div>
    </article>
    <article class="sleeve case-orange">
      <div class="sleeve__brand">VAXEL</div>
      <div class="sleeve__band">PHONE CASE PROTECTION</div>
      <svg class="sleeve__layers" width="72" height="70" viewBox="0 0 72 70" aria-hidden="true">
        <rect x="0" y="14" width="46" height="52" rx="7" fill="var(--grey-3)"/>
        <rect x="9" y="8" width="46" height="52" rx="7" fill="var(--grey-2)"/>
        <rect x="18" y="2" width="46" height="52" rx="7" fill="var(--grey-1)"/>
      </svg>
      <div class="badge badge--layer"><span class="badge__num">2</span>EXTRA LAYER<br>PROTECTION</div>
      <div class="badge badge--scratch">SCRATCH<br>RESISTANT</div>
      <div class="badge badge--top"><span class="badge__big">TOP</span><span class="badge__small">QUALITY</span></div>
      <div class="sleeve__window"><span class="sleeve__case"></span></div>
      <div class="sleeve__claim">COMPATIBLE WITH 99% PHONES</div>
    </article>
    <article class="sleeve case-purple">
      <div class="sleeve__brand">VAXEL</div>
      <div class="sleeve__band">PHONE CASE PROTECTION</div>
      <svg class="sleeve__layers" width="72" height="70" viewBox="0 0 72 70" aria-hidden="true">
        <rect x="0" y="14" width="46" height="52" rx="7" fill="var(--grey-3)"/>
        <rect x="9" y="8" width="46" height="52" rx="7" fill="var(--grey-2)"/>
        <rect x="18" y="2" width="46" height="52" rx="7" fill="var(--grey-1)"/>
      </svg>
      <div class="badge badge--layer"><span class="badge__num">2</span>EXTRA LAYER<br>PROTECTION</div>
      <div class="badge badge--scratch">SCRATCH<br>RESISTANT</div>
      <div class="badge badge--top"><span class="badge__big">TOP</span><span class="badge__small">QUALITY</span></div>
      <div class="sleeve__window"><span class="sleeve__case"></span></div>
      <div class="sleeve__claim">COMPATIBLE WITH 99% PHONES</div>
    </article>
  </main>

  <section class="versions">
    <h2 class="versions__title">DIFFERENT LOGO VERSIONS</h2>
    <div class="versions__tile tile--a">VAXEL</div>
    <div class="versions__tile tile--b">VAXEL</div>
    <div class="versions__tile tile--c">VAXEL</div>
    <div class="versions__tile tile--d">VAXEL</div>
  </section>
</body>
</html>
```